Brenford Automotive business card
Business card design for Brenford Automotive
Project: Brenford Automotive business card
Brenford Automotive business card - Automotive
Creative Brief
Simple
Wade Pelling
482 Kettle Lane Madison, WI 53790
brenautoco@mailnest.example
Hours: Mon-Thurs 7am-6pm
I want a simple road map on the back of the card, with the business location indicated with a star. The map should include Hwy 37, Hwy 21-29, Quarry Bend Rd, Larkfield Loop / Denholm St, Trobek Rd, Kettle Ln, and Corvell Rd.

```html
<!DOCTYPE html>
<html lang="en">
<head>
<meta charset="utf-8">
<title>Brenford Automotive — Business Card</title>
<link href="https://fonts.googleapis.com/css2?family=Arimo:wght@400;700&display=swap" rel="stylesheet">
<style>
  :root {
    --page-bg: #e9e6e1;
    --card-white: #ffffff;
    --card-fade: #eef0f2;
    --brand-blue: #1f7ccc;
    --ink-dark: #2f3338;
    --ink-text: #3d4148;
    --rule: #b9bdc2;
  }
  html, body {
    margin: 0;
    padding: 0;
    width: 1200px;
    height: 965px;
    overflow: hidden;
    background: var(--page-bg);
    font-family: "Arimo", Arial, sans-serif;
  }
  .card {
    position: absolute;
    left: 100px;
    top: 202px;
    width: 1000px;
    height: 561px;
    border-radius: 34px;
    overflow: hidden;
    box-shadow: 0 10px 30px rgba(0,0,0,0.18);
  }
  .card-shapes {
    position: absolute;
    inset: 0;
  }
  .wordmark {
    position: absolute;
    left: 0;
    right: 0;
    top: 190px;
    display: flex;
    justify-content: center;
    align-items: center;
    gap: 18px;
  }
  .wordmark-dot {
    width: 22px;
    height: 22px;
    border-radius: 50%;
    background: var(--brand-blue);
  }
  .wordmark-name {
    font-weight: 700;
    font-size: 62px;
    color: var(--ink-dark);
    letter-spacing: 0.5px;
  }
  .contact-name {
    position: absolute;
    right: 530px;
    top: 424px;
    font-size: 34px;
    font-weight: 700;
    color: var(--brand-blue);
    white-space: nowrap;
  }
  .divider {
    position: absolute;
    left: 498px;
    top: 378px;
    width: 2px;
    height: 140px;
    background: var(--rule);
  }
  .details {
    position: absolute;
    left: 520px;
    top: 376px;
    font-size: 22px;
    line-height: 35px;
    color: var(--ink-text);
  }
  .details-line {
    display: flex;
    align-items: center;
    gap: 10px;
    white-space: nowrap;
  }
  .details-icon {
    width: 20px;
    height: 20px;
    flex: none;
  }
</style>
</head>
<body>
  <div class="card">
    <svg class="card-shapes" width="1000" height="561" viewBox="0 0 1000 561">
      <defs>
        <linearGradient id="card-face" x1="0" y1="0" x2="0" y2="1">
          <stop offset="0" stop-color="#ffffff"/>
          <stop offset="1" stop-color="#eef0f2"/>
        </linearGradient>
        <linearGradient id="band-blue" x1="0" y1="0" x2="1" y2="1">
          <stop offset="0" stop-color="#3a9be6"/>
          <stop offset="1" stop-color="#1566b0"/>
        </linearGradient>
      </defs>
      <rect width="1000" height="561" fill="url(#card-face)"/>
      <path d="M0 40 C60 160 80 380 110 561 L0 561 Z" fill="url(#band-blue)"/>
      <path d="M900 0 C930 150 940 350 935 561 L1000 561 L1000 0 Z" fill="#1b1d20"/>
      <path d="M915 0 C950 150 960 330 952 561 L1000 561 L1000 0 Z" fill="url(#band-blue)"/>
    </svg>

    <div class="wordmark">
      <span class="wordmark-dot"></span>
      <span class="wordmark-name">Brenford Automotive</span>
    </div>

    <div class="contact-name">Wade Pelling</div>
    <div class="divider"></div>

    <div class="details">
      <div class="details-line">482 Kettle Lane</div>
      <div class="details-line">Madison, WI 53790</div>
      <div class="details-line">
        <svg class="details-icon" viewBox="0 0 24 24" aria-hidden="true">
          <path d="M6 3 C4 4 3 6 4 9 C6 15 10 19 16 21 C18 22 20 21 21 18 L17 15 L15 17 C12 16 9 13 8 10 L10 8 Z" fill="#1f7ccc"/>
        </svg>
        (608) 555-0142
      </div>
      <div class="details-line">
        <svg class="details-icon" viewBox="0 0 24 24" aria-hidden="true">
          <text x="12" y="19" text-anchor="middle" font-family="Arimo, Arial, sans-serif" font-weight="700" font-size="22" fill="#1f7ccc">@</text>
        </svg>
        brenautoco@mailnest.example
      </div>
    </div>
  </div>
</body>
</html>
```